business card deign

Logo needs the following on it.
1. attached logo
2. Tagline - "When the cooler stays full and the night rolls on...that's us!"
3. Name- Delia Fenwick, Founder and CPO
4. Address - 418 E. Harlow Avenue, Ste 2204, Tampa, FL. 33719
5. Phone - 720.555.0187

```html
<!DOCTYPE html>
<html lang="en">
<head>
<meta charset="utf-8">
<title>Koolari Business Card</title>
<link rel="stylesheet" href="https://fonts.googleapis.com/css2?family=Montserrat:wght@400;500;600;700&display=swap">
<style>
  :root {
    --bg: #3a3a3a;
    --card-dark: #2e2e2e;
    --card-back: #2a2a2a;
    --paper: #ffffff;
    --ink: #141414;
    --muted: #9a9a9a;
    --rule: #555555;
    --silver: #8d8d8d;
  }
  * { box-sizing: border-box; margin: 0; padding: 0; }
  html, body { width: 1200px; height: 1200px; overflow: hidden; }
  body {
    background: var(--bg);
    font-family: "Montserrat", sans-serif;
    display: flex;
    flex-direction: column;
    align-items: center;
    justify-content: center;
    gap: 44px;
  }
  .card {
    position: relative;
    width: 900px;
    height: 514px;
    border-radius: 40px;
    overflow: hidden;
    box-shadow: 0 14px 30px rgba(0,0,0,0.45);
  }
  /* Front */
  .card-front { background: var(--card-dark); }
  .front-top {
    position: absolute; left: 0; top: 0; width: 100%; height: 290px;
    background: var(--paper);
  }
  .front-stripe {
    position: absolute; left: 0; top: 290px; width: 100%; height: 12px;
    background: var(--card-dark);
  }
  .front-gap {
    position: absolute; left: 0; top: 302px; width: 100%; height: 9px;
    background: var(--paper);
  }
  .brand {
    position: absolute; display: flex; align-items: center; gap: 18px;
  }
  .brand-front { left: 230px; top: 118px; }
  .brand-mark {
    width: 34px; height: 34px; border-radius: 50%; background: var(--ink);
  }
  .brand-name {
    font-weight: 600; font-size: 44px; letter-spacing: 14px; color: var(--ink);
  }
  .person {
    position: absolute; left: 110px; top: 372px; color: var(--paper);
  }
  .person-name { font-weight: 700; font-size: 34px; letter-spacing: 0.5px; }
  .person-title { font-weight: 400; font-size: 22px; letter-spacing: 0.5px; margin-top: 2px; }
  .divider {
    position: absolute; left: 470px; top: 330px; width: 1px; height: 150px;
    background: var(--rule);
  }
  .contact {
    position: absolute; left: 510px; top: 340px; color: var(--paper);
    font-size: 22px; line-height: 1.3; list-style: none;
  }
  .contact li { display: flex; align-items: flex-start; gap: 12px; margin-bottom: 10px; }
  .contact svg { width: 22px; height: 22px; flex: none; margin-top: 3px; fill: var(--paper); }
  /* Back */
  .card-back { background: var(--card-back); }
  .brand-back {
    left: 0; right: 0; top: 200px; justify-content: center;
  }
  .brand-back .brand-mark { background: var(--silver); width: 40px; height: 40px; }
  .brand-back .brand-name { color: var(--silver); font-size: 60px; letter-spacing: 18px; }
  .tagline {
    position: absolute; left: 0; right: 0; top: 400px; text-align: center;
    color: var(--muted); font-weight: 600; font-size: 25px;
  }
</style>
</head>
<body>
  <section class="card card-front">
    <div class="front-top"></div>
    <div class="front-stripe"></div>
    <div class="front-gap"></div>
    <div class="brand brand-front">
      <span class="brand-mark"></span>
      <span class="brand-name">KOOLARI</span>
    </div>
    <div class="person">
      <div class="person-name">DELIA FENWICK</div>
      <div class="person-title">FOUNDER AND CPO</div>
    </div>
    <div class="divider"></div>
    <ul class="contact">
      <li>
        <svg viewBox="0 0 24 24" aria-hidden="true"><path d="M6.6 10.8a15.1 15.1 0 0 0 6.6 6.6l2.2-2.2a1 1 0 0 1 1-.25 11.4 11.4 0 0 0 3.6.57 1 1 0 0 1 1 1V20a1 1 0 0 1-1 1A17 17 0 0 1 3 4a1 1 0 0 1 1-1h3.5a1 1 0 0 1 1 1c0 1.250.2 2.450.57 3.57a1 1 0 0 1-.25 1z"/></svg>
        <span>720.555.0187</span>
      </li>
      <li>
        <svg viewBox="0 0 24 24" aria-hidden="true"><path d="M12 2a7 7 0 0 0-7 7c0 5.2 7 13 7 13s7-7.8 7-13a7 7 0 0 0-7-7zm0 9.5A2.5 2.5 0 1 1 12 6.5a2.5 2.5 0 0 1 0 5z"/></svg>
        <span>418 E. Harlow Avenue,<br>Ste 2204, Tampa, FL. 33719</span>
      </li>
    </ul>
  </section>

  <section class="card card-back">
    <div class="brand brand-back">
      <span class="brand-mark"></span>
      <span class="brand-name">KOOLARI</span>
    </div>
    <p class="tagline">When the cooler stays full and the night rolls on...that's us!</p>
  </section>
</body>
</html>
```